BRMSC redesign and update stationary bc envelopes.

Stationary, Envelopes, Brochures, Business Card. Need to add second surgeon and two other offices. I need everything to match. I am a oral & maxillofacial surgeon.
Additional surgeon and three office addresses.
Tae Woo Park, DMD, MD, INC

3178 Silver Meadow Boulevard
El Dorado Hills, CA 95762

612 Lorel Lane, Suite 101
Folsom, CA. 95630

2375 Birch Avenue, Suite 105
Auburn, CA. 95603
Updates

Logo design uploaded. Zapfino Extra/Adobe Garamond/Palatino are fonts used before. Not sure what is on exisiting stationary.

Target Market(s)

Referral dentist and sometimes patients. I am a oral & Maxillofacial surgeon.

Industry/Entity Type

Dental Clinic

Font styles to use
Serif
Script

Requirements
Must have
• Color of existing stationary. Update is possible.
Nice to have
• Conservative/modern
Should not have
• Playful

```html
<!DOCTYPE html>
<html lang="en">
<head>
<meta charset="utf-8">
<title>BRMSC Business Card</title>
<link rel="stylesheet" href="https://fonts.googleapis.com/css2?family=PT+Serif&family=Libre+Caslon+Text:wght@700&family=Roboto&display=swap">
<style>
:root{
  --bg:#e6e6e4;
  --card:#ffffff;
  --brown:#5a4037;
  --band:#6b4f41;
  --green:#6a9a24;
  --seal:#c9d6b3;
}
html,body{margin:0;padding:0;width:1188px;height:1200px;overflow:hidden;background:var(--bg);}
.card{position:absolute;left:245px;width:696px;height:386px;background:var(--card);box-shadow:0 10px 18px rgba(0,0,0,.18);font-family:"PT Serif",serif;color:var(--brown);overflow:hidden;}
.card--front{top:159px;}
.card--back{top:627px;}
.brand{position:absolute;display:flex;align-items:center;gap:12px;font-family:"PT Serif",serif;color:var(--brown);}
.brand__dot{border-radius:50%;background:var(--green);}
.card--front .brand{left:55px;top:95px;font-size:44px;}
.card--front .brand__dot{width:26px;height:26px;}
.card--back .brand{left:0;right:0;top:96px;justify-content:center;font-size:62px;}
.card--back .brand__dot{width:34px;height:34px;}
.surgeon{position:absolute;right:41px;top:73px;margin:0;font-family:"Libre Caslon Text",serif;font-weight:700;font-size:22px;white-space:nowrap;}
.board{position:absolute;right:83px;top:106px;text-align:right;font-family:"Roboto",sans-serif;color:var(--green);font-size:15px;line-height:19px;}
.seal{position:absolute;right:41px;top:108px;width:34px;height:34px;border-radius:50%;background:var(--seal);}
.lines{position:absolute;font-size:18px;line-height:22.5px;white-space:nowrap;}
.main-office{right:41px;top:196px;text-align:right;}
.contact{right:41px;top:248px;text-align:right;line-height:23.5px;}
.contact div{display:flex;justify-content:flex-end;align-items:center;gap:7px;}
.contact svg{width:16px;height:16px;fill:var(--green);}
.branch{left:55px;}
.branch--auburn{top:248px;}
.branch--folsom{top:298px;}
.services{position:absolute;left:0;right:0;top:256px;text-align:center;font-size:17px;line-height:22.5px;}
.services .dot{color:var(--green);font-size:12px;margin:0 3px;vertical-align:1px;}
.rule{position:absolute;left:0;right:0;top:339px;height:3px;background:var(--green);}
.web-band{position:absolute;left:0;right:0;top:345px;height:41px;background:var(--band);color:#fff;text-align:center;line-height:41px;font-size:21px;}
</style>
</head>
<body>
<section class="card card--front">
  <div class="brand"><span class="brand__dot"></span>BRMSC</div>
  <h1 class="surgeon">Tae Woo Park, DMD, MD, INC</h1>
  <div class="board">Diplomate of the National Board of<br>Facial &amp; Jaw Surgery</div>
  <div class="seal" role="img" aria-label="Board certification seal"></div>
  <div class="lines main-office">3178 Silver Meadow Boulevard<br>El Dorado Hills, CA 95762</div>
  <div class="lines contact">
    <div>916.555.0142 <svg viewBox="0 0 16 16"><path d="M2 6c0-2 3-3 6-3s6 1 6 3v1h-3V6H5v1H2zM4 8h8l2 6H2z"/></svg></div>
    <div>916.555.0187 <svg viewBox="0 0 16 16"><path d="M4 1h8v4H4zM1 6h14v6h-3v3H4v-3H1zM5 10v3h6v-3z"/></svg></div>
    <div>drpark@silvermeadowoms.com <svg viewBox="0 0 16 16"><path d="M1 3h14v10H1zm1 1l6 5 6-5z"/></svg></div>
    <div>www.silvermeadowoms.com <svg viewBox="0 0 16 16"><circle cx="8" cy="8" r="7"/><path d="M5 4c2 0 3 2 2 4s1 3 0 5M10 3c0 2 2 2 3 4" stroke="#fff" stroke-width="1.3" fill="none"/></svg></div>
  </div>
  <div class="lines branch branch--auburn">2375 Birch Avenue, Suite 105<br>Auburn, CA. 95603</div>
  <div class="lines branch branch--folsom">612 Lorel Lane, Suite 101<br>Folsom, CA. 95630</div>
</section>

<section class="card card--back">
  <div class="brand"><span class="brand__dot"></span>BRMSC</div>
  <div class="services">
    <span class="dot">●</span>Dentoalveolar Surgery <span class="dot">●</span>Dental Implant Surgery <span class="dot">●</span>Orthognathic Surgery<br>
    <span class="dot">●</span>Facial Trauma Surgery <span class="dot">●</span>Preprosthetic and Reconstructive Surgery<br>
    <span class="dot">●</span>TMJ Disorders and Surgery <span class="dot">●</span>Obstructive Sleep Apnea Surgery
  </div>
  <div class="rule"></div>
  <div class="web-band">www.silvermeadowoms.com</div>
</section>
</body>
</html>
```